Criação de Capa para Facebook para Horizonte & Saberes
" Nossos clientes solicitam softwares personalizados para rodarem em suas empresas. Desenhamos um projeto de software e temos uma equipe de desenvolvedores para executar a construção do software. Nosso foco é em sistemas web e aplicativos para celular. "

```html
<!DOCTYPE html>
<html lang="pt-BR">
<head>
<meta charset="utf-8">
<title>Horizonte &amp; Saberes — Capa para Facebook</title>
<link rel="stylesheet" href="https://fonts.googleapis.com/css2?family=Montserrat:wght@400;500;600&display=swap">
<style>
  :root {
    --page-bg: #eef1f3;
    --navy-deep: #0a1e30;
    --navy: #12304a;
    --teal: #19a985;
    --grey-panel: #c3cad2;
    --white: #ffffff;
    --text-soft: #d7e2ec;
  }
  * { margin: 0; padding: 0; box-sizing: border-box; }
  html, body {
    width: 1200px;
    height: 1200px;
    overflow: hidden;
    background: var(--page-bg);
    font-family: "Montserrat", sans-serif;
  }
  .cover {
    position: absolute;
    left: 40px;
    top: 392px;
    width: 1120px;
    height: 416px;
    background: linear-gradient(100deg, var(--navy-deep) 0%, var(--navy) 55%, var(--navy-deep) 100%);
    overflow: hidden;
  }
  .cover__network {
    position: absolute;
    left: 0;
    top: 0;
    width: 640px;
    height: 400px;
    background: radial-gradient(ellipse at 35% 50%, rgba(45, 100, 145, 0.55) 0%, rgba(29, 74, 110, 0.25) 45%, rgba(10, 30, 48, 0) 75%);
  }
  .cover__side-block {
    position: absolute;
    left: 850px;
    top: 40px;
    width: 270px;
    height: 330px;
    background: var(--grey-panel);
  }
  .cover__accent-strip {
    position: absolute;
    left: 0;
    bottom: 0;
    width: 100%;
    height: 14px;
    background: var(--teal);
  }
  .cover__content {
    position: absolute;
    left: 90px;
    top: 118px;
    width: 720px;
    display: flex;
    flex-direction: column;
    align-items: center;
    text-align: center;
  }
  .brand {
    display: flex;
    align-items: center;
    gap: 16px;
    white-space: nowrap;
  }
  .brand__square {
    flex: none;
    width: 30px;
    height: 30px;
    background: var(--teal);
  }
  .brand__name {
    color: var(--white);
    font-weight: 500;
    font-size: 40px;
    letter-spacing: 2px;
    text-transform: uppercase;
    line-height: 1;
  }
  .tagline {
    margin-top: 38px;
    color: var(--text-soft);
    font-weight: 500;
    font-size: 16px;
    white-space: nowrap;
  }
  .contacts {
    margin-top: 34px;
    margin-left: 120px;
    display: flex;
    gap: 34px;
    color: var(--white);
    font-size: 14px;
    font-weight: 500;
    white-space: nowrap;
  }
  .contact {
    display: flex;
    align-items: center;
    gap: 9px;
  }
  .contact__icon {
    width: 22px;
    height: 22px;
  }
</style>
</head>
<body>
  <section class="cover">
    <div class="cover__network" role="img" aria-label="Globo digital com rede de pontos e linhas conectadas"></div>
    <div class="cover__side-block"></div>

    <div class="cover__content">
      <div class="brand">
        <span class="brand__square"></span>
        <span class="brand__name">Horizonte &amp; Saberes</span>
      </div>
      <p class="tagline">Soluções em TI que transformam objetivos em resultados</p>
      <div class="contacts">
        <span class="contact">
          <svg class="contact__icon" viewBox="0 0 24 24">
            <circle cx="12" cy="12" r="12" fill="#19a985"/>
            <path d="M8.6 6.5l1.8 0 .9 2.8-1.3 1c.7 1.5 1.8 2.6 3.3 3.3l1-1.3 2.8.9 0 1.8c0 .6-.5 1-1.1 1C11 16 8 13 7.5 7.6c0-.6.5-1.1 1.1-1.1z" fill="#0a1e30"/>
          </svg>
          (00) 0000-0000
        </span>
        <span class="contact">
          <svg class="contact__icon" viewBox="0 0 24 24">
            <circle cx="12" cy="12" r="12" fill="#19a985"/>
            <g fill="none" stroke="#0a1e30" stroke-width="1.4">
              <circle cx="12" cy="12" r="5.5"/>
              <ellipse cx="12" cy="12" rx="2.4" ry="5.5"/>
              <line x1="6.5" y1="12" x2="17.5" y2="12"/>
            </g>
          </svg>
          www.empresa.com.br
        </span>
      </div>
    </div>

    <div class="cover__accent-strip"></div>
  </section>
</body>
</html>
```